Visitenkarte erstellen für Reiki Praxis

Visitenkarten für Reiki Praxis Doppelseitig

business cards reiki practice double-sided

The background can also be a different color

```html
<!DOCTYPE html>
<html lang="en">
<head>
<meta charset="utf-8">
<title>Quiet Lotus Healing – Business Cards</title>
<link href="https://fonts.googleapis.com/css2?family=Ubuntu:wght@400&family=Quicksand:wght@400;500&display=swap" rel="stylesheet">
<style>
  :root {
    --stage: #5a5a5c;
    --card: #1a1a1a;
    --white: #ffffff;
    --gold: #e2ad2f;
    --pattern-dark: #1b1b1b;
    --pattern-light: #3a3a3c;
    --logo-line: #d8c3bd;
    --icon: #b99a8e;
  }
  * { margin: 0; padding: 0; box-sizing: border-box; }
  html, body { width: 900px; height: 1200px; overflow: hidden; }
  body {
    background: var(--stage);
    position: relative;
    font-family: "Quicksand", sans-serif;
    color: var(--white);
  }
  .card {
    position: absolute;
    left: 171px;
    width: 562px;
    height: 362px;
    border-radius: 30px;
    background: var(--card);
    overflow: hidden;
  }
  .card--front { top: 196px; }
  .card--back { top: 630px; }

  .front-pattern {
    position: absolute; inset: 0;
    background: linear-gradient(100deg, var(--pattern-dark) 0%, var(--pattern-dark) 35%, var(--pattern-light) 100%);
  }
  .front-mark {
    position: absolute;
    left: 251px; top: 153px;
    width: 60px; height: 60px;
    border: 1.5px solid var(--logo-line);
    border-radius: 50%;
  }
  .front-title {
    position: absolute; left: 0; right: 0; top: 240px;
    text-align: center;
    font-family: "Ubuntu", sans-serif;
    font-weight: 400;
    font-size: 25px;
    line-height: 1.1;
    letter-spacing: 0.3px;
    color: var(--white);
  }
  .front-name {
    position: absolute; left: 0; right: 0; top: 268px;
    text-align: center;
    font-size: 19px;
    line-height: 1.1;
    letter-spacing: 6px;
    color: var(--gold);
    font-weight: 500;
  }

  .back-decoration {
    position: absolute; inset: 0;
    background: radial-gradient(ellipse 260px 150px at 50% 52%, #202020 0%, var(--card) 100%);
  }
  .back-identity {
    position: absolute; right: 301px; top: 158px;
    text-align: right;
  }
  .back-name { font-size: 23px; color: var(--gold); font-weight: 500; letter-spacing: 1px; line-height: 1.1; }
  .back-role { font-size: 14px; margin-top: 4px; line-height: 1.1; }
  .back-divider {
    position: absolute; left: 279px; top: 146px;
    width: 2px; height: 70px; background: var(--white);
  }
  .contact-list {
    position: absolute; left: 296px; top: 143px;
    list-style: none;
    font-size: 14px; letter-spacing: 0.5px;
  }
  .contact-list li { display: flex; align-items: center; height: 26px; white-space: nowrap; }
  .contact-list svg { width: 12px; height: 12px; margin-right: 7px; flex: none; }
  .follow {
    position: absolute; left: 0; right: 0; top: 310px;
    display: flex; justify-content: center; align-items: center; gap: 8px;
    font-size: 14px; letter-spacing: 0.5px;
  }
  .follow-handle { color: var(--gold); font-weight: 500; }
  .follow-dot { width: 16px; height: 16px; border: 2px solid var(--gold); border-radius: 50%; }
</style>
</head>
<body>
  <section class="card card--front">
    <div class="front-pattern" role="img" aria-label="Repeating line pattern of lotus flowers fading from black to silver grey"></div>
    <div class="front-mark"></div>
    <h1 class="front-title">QUIET LOTUS HEALING</h1>
    <p class="front-name">MARA LIND</p>
  </section>

  <section class="card card--back">
    <div class="back-decoration" role="img" aria-label="Large faint lotus line drawing behind the contact details"></div>
    <div class="back-identity">
      <p class="back-name">MARA LIND</p>
      <p class="back-role">Founder</p>
    </div>
    <div class="back-divider"></div>
    <ul class="contact-list">
      <li>
        <svg viewBox="0 0 12 12"><path d="M2 1 L4 1 L5 4 L3.8 5 C4.5 6.6 5.5 7.6 7 8.2 L8 7 L11 8 L11 10 C11 10.6 10.5 11 10 11 C5 11 1 7 1 2 C1 1.5 1.4 1 2 1 Z" fill="var(--icon)"/></svg>
        07700 900461
      </li>
      <li>
        <svg viewBox="0 0 12 12"><rect x="0.5" y="2" width="11" height="8" fill="#c9a9a3"/><path d="M0.5 2 L6 7 L11.5 2" stroke="#1a1a1a" fill="none" stroke-width="1"/></svg>
        mara.lind@example.com
      </li>
      <li>
        <svg viewBox="0 0 12 12"><circle cx="6" cy="6" r="5" fill="none" stroke="var(--icon)" stroke-width="1"/><path d="M1 6 H11 M6 1 V11 M2.5 3.5 H9.5 M2.5 8.5 H9.5" stroke="var(--icon)" stroke-width="0.8"/></svg>
        www.quietlotus.example
      </li>
    </ul>
    <div class="follow">
      <span>follow us on:</span>
      <span class="follow-dot"></span>
      <span class="follow-handle">@quietlotus</span>
    </div>
  </section>
</body>
</html>
```